Derek Osei Consulting

I've the wording, and the rough layout. See attached MicroSoft Word File. I need a professional to make my postcard "look pretty".

Industry/Entity Type

Consulting

```html
<!DOCTYPE html>
<html lang="en">
<head>
<meta charset="utf-8">
<title>Derek Osei Consulting – Postcard</title>
<link href="https://fonts.googleapis.com/css2?family=Arimo:wght@400;700&display=swap" rel="stylesheet">
<style>
  :root {
    --navy: #3b4a9c;
    --green: #6dbd45;
    --sky: #29a3dc;
    --plum: #a24f9c;
    --rose: #e8215e;
    --white: #ffffff;
  }
  * { margin: 0; padding: 0; box-sizing: border-box; }
  html, body { width: 1200px; height: 776px; overflow: hidden; background: var(--white); }
  body { font-family: "Arimo", Arial, sans-serif; color: var(--white); }
  .postcard { position: relative; width: 1200px; height: 776px; background: var(--white); }
  .headline {
    position: absolute; top: 0; left: 0; width: 100%; height: 76px;
    display: flex; align-items: center; justify-content: center;
    color: var(--navy); font-size: 24.5px; font-weight: 400;
  }
  .panel { position: absolute; font-size: 18.6px; line-height: 23.6px; overflow: hidden; }
  .questions {
    left: 0; top: 66px; width: 604px; height: 634px;
    background: var(--green); padding: 14px 30px 0 25px;
  }
  .questions ol { list-style: none; }
  .questions li { margin-bottom: 4.5px; }
  .questions .num { margin-right: 12px; }
  .insiders { left: 605px; top: 66px; width: 595px; height: 187px; background: var(--sky); padding: 14px 28px 0 25px; }
  .strugglers { left: 605px; top: 253px; width: 595px; height: 188px; background: var(--plum); padding: 13px 28px 0 25px; }
  .challenge { left: 605px; top: 445px; width: 595px; height: 255px; background: var(--rose); padding: 8px 28px 0 25px; }
  .challenge p { margin-bottom: 2px; }
  .challenge .next { text-align: right; font-weight: 700; }
  .web-address {
    position: absolute; left: 0; top: 700px; width: 100%; height: 72px;
    display: flex; align-items: center; justify-content: center;
    color: var(--navy); font-size: 26px; font-weight: 700;
  }
</style>
</head>
<body>
<main class="postcard">
  <h1 class="headline">Learn Osei Business Insights only “insiders” know about:</h1>

  <section class="panel questions">
    <ol>
      <li><span class="num">1.</span>For those people who almost bought from you but did not, what’s the real reason why they didn’t buy from you? (And what to do about it?)</li>
      <li><span class="num">2.</span>How to turn an ordinary service that the customer can find everywhere, into something that the customer has to buy from you and only you?</li>
      <li><span class="num">3.</span>How to turn customer’s “scope creeping”, from a business loss, into a profit generator?</li>
      <li><span class="num">4.</span>What sort of person would be eager to sell to you at below fair market value?</li>
      <li><span class="num">5.</span>How to best utilize your limited operating capital?</li>
      <li><span class="num">6.</span>What sort of people would be a waste of time for your marketing effort?</li>
      <li><span class="num">7.</span>Other than money, how to motivate your employees?</li>
      <li><span class="num">8.</span>How to prevent your employees from stealing your business secrets? Setting up a competing business down the street from you? And worse still, taking your existing customers too?</li>
      <li><span class="num">9.</span>How to increase the perceived value of your products and services in the mind of your customers?</li>
      <li><span class="num">10.</span>How to market a commodity as a highly desired “must have” luxury item?</li>
      <li><span class="num">11.</span>How do you utilize a potentially bad situation and turn the situation into something positive? productive? and most importantly: Profitable???!!!</li>
    </ol>
  </section>

  <section class="panel insiders">
    <p>“Insiders” who know the answers to these tricky business problems, get ahead in business and life. And the deeper their understanding to these tricky business problems, the more successful they become. They have very little stress from their businesses; they work very few hours by building their businesses into "auto pilot". They have more free time to enjoy life.</p>
  </section>

  <section class="panel strugglers">
    <p>If you don't know how to solve these tricky business problems, you will find yourself struggling with your businesses. You will find yourself working very long hours, and you have a lot of stress from running your business. If you are not even aware of the existence of this aspect of running a business, your business will not survive. You will become part of the statistic: 80% of businesses fail.</p>
  </section>

  <section class="panel challenge">
    <p>What specific problems are slowing you down, or keeping you stuck, from reaching your ultimate goals? What specific challenges are causing you all the Stresses? Headaches? Frustrations?</p>
    <p>If your situation continues, how will it negatively impact you from achieving your personal fulfillment? If these problems and challenges could be solved, what are the benefits to you? Short term benefits? Long term benefits?</p>
    <p>To learn how to overcome these problems and challenges:</p>
    <p class="next">Turn to the other side for more info -&gt;</p>
  </section>

  <p class="web-address">www.OseiBusinessInsights.com</p>
</main>
</body>
</html>
```